依頼詳細
残暑お見舞い申し上げます

コロナ禍と暑さで汗が噴き出るような日々が続きますが、いかがお過ごしでしょうか?
汗はかけばかくほど、老廃物が体内から出て、心も体も健康になります。
汗をかかないようにすることは、決して良いことではありません。
会社にとっても、今年は汗(特別損失)を出せるチャンスです。
個人も会社もたくさんの汗を出して、より健康体になられること、心より祈念申し上げます。

★写真に添える文章:松本清志の最新刊
「伸びる会社へ組み直す」
定価10,780円(税込み)
記載項目
ノルフェン・パートナーズ
松本 清志・長谷 宗一郎・柴田 昌平
希望イメージ
シンプル 複雑
単色 カラフル
暗い 明るい
日常 高級
遊び心 厳粛
未来的 伝統的
女性的 男性的
希望する色
水色系
納品ファイル
• 高解像度JPG (.jpg)
補足説明
■ 選んだ理由

今年はコロナのイベント中止で花火大会もなくなるなかで、
もってこいのデザインでした。
文字の並べ方に工夫が見られ、メッセージとバックのコントラストが素敵でした。
一目見ておしゃれで気に入りました。

■ 提案者全員のお礼・コメント

この度は、ご応募ありがとうございました。
毎回、新たなご提案が来るのが楽しみでした。素敵なご応募をありがとうございました。

```html
<!DOCTYPE html>
<html lang="ja">
<head>
<meta charset="utf-8">
<title>ノルフェン・パートナーズ/残暑見舞いデザイン案</title>
<link rel="stylesheet" href="https://fonts.googleapis.com/css2?family=Noto+Sans+JP:wght@400;500&family=Noto+Serif+JP:wght@400;600&display=swap">
<style>
  :root {
    --paper: #ffffff;
    --ink: #222629;
    --rule: #444;
    --card-aqua: #d6eef0;
    --card-mist: #eef8f8;
    --card-wave: #bfe2e6;
    --ribbon: #3fa77c;
    --ribbon-dark: #2b8763;
    --book: #c0221c;
  }
  html, body { margin: 0; padding: 0; overflow: hidden; }
  body {
    width: 849px; height: 1200px; position: relative;
    background: var(--paper); color: var(--ink);
    font-family: "Noto Serif JP", serif;
  }
  .sheet-title {
    position: absolute; left: 28px; top: 20px; margin: 0;
    font-family: "Noto Sans JP", sans-serif; font-size: 15px; font-weight: 500;
  }
  .sheet-rule {
    position: absolute; left: 20px; right: 20px; top: 52px;
    border-top: 1.5px solid var(--rule);
  }
  .proposal-label {
    position: absolute; left: 770px; top: 902px;
    font-family: "Noto Sans JP", sans-serif; font-size: 12px; font-weight: 500;
  }
  .postcard {
    position: absolute; left: 212px; top: 178px; width: 430px; height: 643px;
    overflow: hidden;
    background:
      radial-gradient(ellipse 70% 30% at 30% 20%, var(--card-wave), transparent 70%),
      radial-gradient(ellipse 80% 25% at 70% 55%, var(--card-wave), transparent 70%),
      radial-gradient(ellipse 70% 30% at 40% 90%, var(--card-wave), transparent 70%),
      linear-gradient(170deg, var(--card-mist), var(--card-aqua));
    box-shadow: 0 0 0 1px #e2e9ea;
  }
  .ribbon-art {
    position: absolute; left: 272px; top: 58px; width: 136px; height: 88px;
    background: linear-gradient(135deg, var(--ribbon), var(--ribbon-dark));
    border-radius: 40% 60% 45% 55%;
    opacity: .85;
  }
  .vertical { writing-mode: vertical-rl; position: absolute; margin: 0; }
  .greeting {
    right: 190px; top: 162px;
    font-size: 19px; font-weight: 600; letter-spacing: .28em;
  }
  .message {
    right: 232px; top: 100px; height: 350px;
    font-size: 10px; line-height: 1.65; letter-spacing: .04em;
  }
  .message p { margin: 0; }
  .signature {
    right: 356px; top: 300px; height: 160px;
    font-size: 10px; line-height: 1.8; letter-spacing: .08em; text-align: end;
  }
  .signature p { margin: 0; }
  .book-cover {
    position: absolute; left: 24px; top: 493px; width: 50px; height: 72px;
    background: linear-gradient(160deg, #d8342c, var(--book));
  }
  .book-note {
    position: absolute; left: 24px; top: 570px; width: 130px; margin: 0;
    font-size: 6.5px; line-height: 1.6;
  }
</style>
</head>
<body>
  <h1 class="sheet-title">ノルフェン・パートナーズ/残暑見舞いデザイン案</h1>
  <div class="sheet-rule"></div>

  <section class="postcard">
    <div class="ribbon-art" role="img" aria-label="緑色の折り紙のリボン飾り"></div>

    <h2 class="vertical greeting">残暑お見舞い申し上げます</h2>

    <div class="vertical message">
      <p>コロナ禍と暑さで汗が噴き出るような日々が続きますが、いかがお過ごしでしょうか?</p>
      <p>汗はかけばかくほど、老廃物が体内から出て、心も体も健康になります。</p>
      <p>汗をかかないようにすることは、決して良いことではありません。</p>
      <p>会社にとっても、今年は汗(特別損失)を出せるチャンスです。</p>
      <p>個人も会社もたくさんの汗を出して、より健康体になられること、心より祈念申し上げます。</p>
    </div>

    <div class="vertical signature">
      <p>ノルフェン・パートナーズ</p>
      <p>松本 清志・長谷 宗一郎・柴田 昌平</p>
    </div>

    <div class="book-cover" role="img" aria-label="最新刊の書籍の表紙写真"></div>
    <p class="book-note">松本清志の最新刊<br>「伸びる会社へ組み直す」<br>定価10,780円(税込み)</p>
  </section>

  <div class="proposal-label">B案</div>
</body>
</html>
```